Business Card for a mobile physiotherapy company

I need a layout for a business card for a mobile physiotherapy company.
Slogan is "Mobile Physiotherapy - Your Road To Recovery"
Phone number is 867-402-5913
Email VantrePhysio@mailbright.ca (subject to change with website)
Website www.VantrePhysio.ca
My name and credentials: Kent Vantre Kent Vantre, BSc(kin), MPT, CAFCI, IMS
Information maybe included: Direct Billing, Services including Physiotherapy, IMS, acupuncture
Maybe include facebook and instagram logos
One side with the logo clean and sharp
Other side with details, try not to look too busy, keep everything concise

```html
<!DOCTYPE html>
<html lang="en">
<head>
<meta charset="utf-8">
<title>Vantre Physio – Business Card</title>
<link href="https://fonts.googleapis.com/css2?family=Roboto:wght@400;500;700&display=swap" rel="stylesheet">
<style>
  :root {
    --page: #dcdcdc;
    --teal: #1b6359;
    --teal-deep: #135a4f;
    --blue: #2c5382;
    --blue-soft: #40608f;
    --ink: #2e2e2e;
    --muted: #4a4a4a;
    --paper: #ffffff;
    --ghost: #dfe4ec;
  }
  * { box-sizing: border-box; margin: 0; padding: 0; }
  html, body { width: 1200px; height: 900px; overflow: hidden; }
  body {
    background: var(--page);
    font-family: "Roboto", Arial, sans-serif;
    position: relative;
  }
  .card {
    position: absolute;
    left: 260px;
    width: 680px;
    height: 388px;
    background: var(--paper);
    overflow: hidden;
    box-shadow: 0 6px 18px rgba(0,0,0,.18);
  }
  /* Front */
  .card--front { top: 42px; }
  .front__field {
    position: absolute; inset: 0 0 68px 0;
    background: linear-gradient(30deg, var(--teal-deep) 0%, #2a6670 50%, var(--blue) 100%);
    display: flex; flex-direction: column; align-items: center; justify-content: center;
    color: var(--paper);
  }
  .brand-name {
    font-weight: 700;
    letter-spacing: .12em;
    text-transform: uppercase;
    display: flex; align-items: center; gap: 14px;
  }
  .brand-name__dot { width: 14px; height: 14px; background: currentColor; }
  .front__field .brand-name { font-size: 46px; margin-top: 20px; }
  .services {
    margin-top: 48px;
    font-size: 17px;
    letter-spacing: .02em;
    display: flex; align-items: center; gap: 26px;
  }
  .services__sep { width: 8px; height: 8px; border-radius: 50%; background: var(--paper); }
  .front__band {
    position: absolute; left: 0; right: 0; bottom: 0; height: 68px;
    display: flex; align-items: center; justify-content: center;
    font-size: 18px; color: var(--ink); letter-spacing: .01em;
  }
  /* Back */
  .card--back { top: 470px; }
  .holder {
    position: absolute; right: 46px; top: 30px; text-align: right;
  }
  .holder__name { font-size: 27px; font-weight: 700; color: var(--blue-soft); }
  .holder__creds { font-size: 16px; color: var(--muted); margin-top: 4px; }
  .holder__bar {
    position: absolute; right: 0; top: 30px; width: 18px; height: 40px; background: var(--teal);
  }
  .back__brand {
    position: absolute; left: 44px; top: 128px;
    color: var(--teal); font-size: 36px;
  }
  .contacts {
    position: absolute; left: 44px; bottom: 46px;
    list-style: none; display: grid; gap: 12px;
  }
  .contacts li {
    display: flex; align-items: center; gap: 14px;
    font-size: 19px; color: var(--ink);
  }
  .contacts__icon {
    width: 26px; height: 26px; border-radius: 50%;
    display: flex; align-items: center; justify-content: center;
    background: var(--blue-soft);
  }
  .contacts li:nth-child(2) .contacts__icon { background: var(--teal); }
  .back__ghost {
    position: absolute; right: -20px; bottom: 34px;
    font-size: 92px; font-weight: 700; color: var(--ghost);
    letter-spacing: .04em;
  }
</style>
</head>
<body>

<section class="card card--front" aria-label="Card front">
  <div class="front__field">
    <div class="brand-name"><span class="brand-name__dot"></span>Vantre Physio</div>
    <div class="services">
      <span>Physiotherapy</span><span class="services__sep"></span>
      <span>IMS</span><span class="services__sep"></span>
      <span>Acupuncture</span>
    </div>
  </div>
  <div class="front__band">Mobile Physiotherapy - Your Road To Recovery</div>
</section>

<section class="card card--back" aria-label="Card back">
  <div class="back__ghost" aria-hidden="true">VANTRE</div>
  <span class="holder__bar"></span>
  <div class="holder">
    <div class="holder__name">Kent Vantre</div>
    <div class="holder__creds">BSc(kin), MPT, CAFCI, IMS</div>
  </div>
  <div class="brand-name back__brand"><span class="brand-name__dot"></span>Vantre Physio</div>
  <ul class="contacts">
    <li>
      <span class="contacts__icon">
        <svg width="14" height="14" viewBox="0 0 24 24" fill="#fff"><path d="M6.6 10.8a15.1 15.1 0 0 0 6.6 6.6l2.2-2.2c.3-.3.7-.4 1-.2 1.1.4 2.3.6 3.6.6.6 0 1 .4 1 1V20c0 .6-.4 1-1 1A17 17 0 0 1 3 4c0-.6.4-1 1-1h3.5c.6 0 1 .4 1 1 0 1.3.2 2.5.6 3.6.1.3 0 .7-.2 1z"/></svg>
      </span>867-402-5913
    </li>
    <li>
      <span class="contacts__icon">
        <svg width="14" height="14" viewBox="0 0 24 24" fill="none" stroke="#fff" stroke-width="2"><rect x="3" y="5" width="18" height="14" rx="1"/><path d="M3 6l9 7 9-7"/></svg>
      </span>VantrePhysio@mailbright.ca
    </li>
    <li>
      <span class="contacts__icon">
        <svg width="15" height="15" viewBox="0 0 24 24" fill="none" stroke="#fff" stroke-width="1.8"><circle cx="12" cy="12" r="9"/><path d="M3 12h18M12 3c3 3 3 15 0 18M12 3c-3 3-3 15 0 18"/></svg>
      </span>www.VantrePhysio.ca
    </li>
  </ul>
</section>

</body>
</html>
```